New Packaging Design Project

Wine packaging redesign. Retail partner requested a redesign of a private label wine. The old label is attached. Our partner liked the Lantern and Briar label and wanted something similar. There will be a logo added to the top of the label

Went on vacation/holiday

```html
<!DOCTYPE html>
<html lang="en">
<head>
<meta charset="utf-8">
<title>Cedar Hollow – Wine Labels</title>
<link rel="stylesheet" href="https://fonts.googleapis.com/css2?family=Cinzel:wght@400;500;600&display=swap">
<style>
  :root {
    --page-bg: #ffffff;
    --ink: #0d0d0d;
    --ink-soft: #222222;
    --rule: #1a1a1a;
    --sand-light: #e9e3cf;
    --sand: #d8ceae;
    --night: #0b0a0b;
    --silver: #d6d6d8;
    --silver-dim: #a9a9ad;
    --mauve: #a56f87;
    --mauve-light: #c79aae;
  }

  * { box-sizing: border-box; margin: 0; padding: 0; }

  html, body {
    width: 1200px;
    height: 880px;
    overflow: hidden;
    background: var(--page-bg);
  }

  .canvas {
    position: relative;
    width: 1200px;
    height: 880px;
    display: flex;
    align-items: center;
    justify-content: space-around;
    padding: 0 70px;
  }

  .label {
    width: 440px;
    height: 760px;
    display: flex;
    flex-direction: column;
    align-items: center;
    padding-top: 58px;
    font-family: "Cinzel", "Times New Roman", serif;
    color: var(--ink);
  }

  .label--red {
    background: var(--night);
    color: var(--silver);
  }

  .label__brand {
    font-weight: 500;
    font-size: 50px;
    line-height: 54px;
    text-align: center;
    letter-spacing: -0.5px;
  }

  .label__mark {
    width: 316px;
    height: 208px;
    margin-top: 60px;
    border-radius: 46% 54% 38% 62% / 42% 40% 60% 58%;
    background: linear-gradient(160deg, var(--ink-soft) 0%, #6b665a 40%, var(--sand) 70%, var(--sand-light) 100%);
  }

  .label--red .label__mark {
    background: linear-gradient(160deg, var(--silver) 0%, var(--silver-dim) 40%, var(--mauve-light) 70%, var(--mauve) 100%);
  }

  .label__style {
    margin-top: 44px;
    font-size: 22px;
    font-weight: 500;
    letter-spacing: 2px;
  }

  .label__varietals {
    width: 236px;
    margin-top: 10px;
    padding: 6px 0 5px;
    border-top: 1px solid var(--rule);
    border-bottom: 1px solid var(--rule);
    text-align: center;
    font-size: 12.5px;
    line-height: 18px;
    letter-spacing: 0.3px;
  }

  .label--red .label__varietals {
    border-color: var(--silver-dim);
  }

  .label__vintage {
    display: flex;
    align-items: center;
    gap: 12px;
    margin-top: 14px;
    font-size: 16px;
    letter-spacing: 1px;
  }

  .label__vintage::before,
  .label__vintage::after {
    content: "";
    width: 18px;
    height: 1px;
    background: currentColor;
  }
</style>
</head>
<body>
  <main class="canvas">
    <section class="label label--white">
      <h1 class="label__brand">Cedar<br>Hollow</h1>
      <div class="label__mark" role="img" aria-label="Brushstroke illustration of rolling hills over vineyard rows in black ink with a sand-coloured wash"></div>
      <h2 class="label__style">White Blend</h2>
      <p class="label__varietals">Merlot | Cabernet Sauvignon<br>Cabernet Franc | Petit Verdot<br>Malbec</p>
      <p class="label__vintage">2020</p>
    </section>

    <section class="label label--red">
      <h1 class="label__brand">Cedar<br>Hollow</h1>
      <div class="label__mark" role="img" aria-label="Brushstroke illustration of rolling hills over vineyard rows in silver with a mauve wash"></div>
      <h2 class="label__style">Red Blend</h2>
      <p class="label__varietals">Merlot | Cabernet Sauvignon<br>Cabernet Franc | Petit Verdot<br>Malbec</p>
      <p class="label__vintage">2020</p>
    </section>
  </main>
</body>
</html>
```